BUSINESS CARD - HALVERDINE RURAL SERVICES

I would like to create a business card for my fertilizer spreading business. I would like to incorporate my existing logo and also a description of the services offered. The business card will be given to farmers so must be kept simple but effective. It will also be left in stores so much also be eye catching in order to stand out from other cards.

Target Market(s)

FARMERS

Requirements
Must have
• FRONT OF CARD = EXISTING LOGO + "CUSTOMISED SPREADING" below the logo

REAR Of CARD = SERVICES OFFERED AND CONTACT DETAILS

- Bulk fertilizer including Lime, Gypsum, Manure & Compost
- Granular fertilizer including Single Super, Urea, Granomix, & Custom Blends
- Modern equipment - Autosteer & Variable Rate Capable
- Friendly & Reliable Service
- Contact Gus: 0471 502 318
Nice to have
• utilize same color scheme as existing logo

```html
<!DOCTYPE html>
<html lang="en">
<head>
<meta charset="utf-8">
<title>Halverdine Rural Services – Business Card</title>
<link rel="stylesheet" href="https://fonts.googleapis.com/css2?family=Open+Sans:wght@400;600;700&display=swap">
<style>
  :root {
    --page: #ffffff;
    --charcoal: #58585a;
    --ink: #505052;
    --orange: #f39a2b;
    --white: #ffffff;
    --shadow: rgba(0, 0, 0, 0.22);
  }
  * { box-sizing: border-box; margin: 0; padding: 0; }
  html, body {
    width: 1200px;
    height: 1000px;
    overflow: hidden;
    background: var(--page);
    font-family: "Open Sans", Arial, sans-serif;
  }
  .canvas { position: relative; width: 1200px; height: 1000px; }

  .card {
    position: absolute;
    top: 238px;
    width: 300px;
    height: 524px;
    border-radius: 38px;
    box-shadow: 4px 6px 14px var(--shadow);
    text-align: center;
  }
  .card--front { left: 275px; background: var(--charcoal); }
  .card--back  { left: 626px; background: var(--white); color: var(--ink); }

  .front-ring {
    position: absolute;
    left: 27px;
    top: 139px;
    width: 246px;
    height: 246px;
    border-radius: 50%;
    border: 1.5px solid var(--white);
  }
  .front-emblem {
    position: absolute;
    left: 38px;
    top: 150px;
    width: 224px;
    height: 224px;
    border-radius: 50%;
    background: var(--white);
    display: flex;
    align-items: center;
    justify-content: center;
  }
  .brand-name {
    font-weight: 700;
    color: var(--ink);
    line-height: 1.15;
    letter-spacing: 0.02em;
  }
  .front-emblem .brand-name { font-size: 19px; }
  .tagline {
    position: absolute;
    left: 0;
    right: 0;
    top: 418px;
    color: var(--white);
    font-size: 15px;
    line-height: 20px;
    letter-spacing: 0.03em;
  }

  .back-brand {
    position: absolute;
    left: 0; right: 0; top: 38px;
    display: flex;
    flex-direction: column;
    align-items: center;
  }
  .brand-dot {
    width: 70px; height: 70px;
    border-radius: 50%;
    background: var(--charcoal);
  }
  .back-brand .brand-name { font-size: 17px; line-height: 22px; margin-top: 21px; }

  .services {
    position: absolute;
    left: 45px; right: 45px; top: 184px;
    list-style: none;
  }
  .service-title { font-weight: 600; font-size: 14px; line-height: 18px; letter-spacing: 0.02em; }
  .service-detail { font-size: 14px; line-height: 18px; }
  .divider { height: 2px; background: var(--orange); margin: 10px 0 9px; }

  .contact { position: absolute; left: 0; right: 0; top: 409px; }
  .contact-label { font-size: 14px; line-height: 20px; }
  .contact-name { font-size: 24px; line-height: 28px; }
  .contact-phone { font-size: 25px; line-height: 32px; font-weight: 600; margin-top: 3px; letter-spacing: 0.02em; }
</style>
</head>
<body>
<main class="canvas">
  <section class="card card--front" aria-label="Card front">
    <span class="front-ring" aria-hidden="true"></span>
    <div class="front-emblem">
      <p class="brand-name">HALVERDINE RURAL<br>SERVICES</p>
    </div>
    <p class="tagline">CUSTOMISED SPREADING</p>
  </section>

  <section class="card card--back" aria-label="Card back">
    <div class="back-brand">
      <span class="brand-dot"></span>
      <p class="brand-name">HALVERDINE RURAL SERVICES</p>
    </div>
    <ul class="services">
      <li class="service">
        <p class="service-title">BULK FERTILIZER</p>
        <p class="service-detail">including Lime, Gypsum,<br>Manure &amp; Composts</p>
      </li>
      <li class="divider" aria-hidden="true"></li>
      <li class="service">
        <p class="service-title">GRANULAR FERTILIZER</p>
        <p class="service-detail">including Single Super, Urea,<br>Granomix, &amp; Custom Blends</p>
      </li>
      <li class="divider" aria-hidden="true"></li>
      <li class="service"><p class="service-title">MODERN EQUIPMENT</p></li>
      <li class="divider" aria-hidden="true"></li>
      <li class="service"><p class="service-title">FRIENDLY &amp; RELIABLE SERVICE</p></li>
    </ul>
    <div class="contact">
      <p class="contact-label">CONTACT :</p>
      <p class="contact-name">Gus</p>
      <p class="contact-phone">0471 502 318</p>
    </div>
  </section>
</main>
</body>
</html>
```